About the book: It is an A5 size book, small 40 pages miniguide
Book title: The pocket handbook of home lending
Book subtitle: The quiet road to plenty
Author: Ned Pargiter
Back cover content: Please see attached word document "back page"
Colours: Our company logo should go at the back of the book. One colour we can't use is red. As this is a finance book the red colour is seen negatively. may be light green? you are the expert.
I think lots of white space will work well.
NOTE: please read the back cover notes to get an understanding of what the book is about. It educates readers about finance in property investing. It makes sense that image used combines 'property' and 'finance'. please read back page document attached.
NOTE: it is a small A5 , 40 page book . Its a miniguide rather than a book .

Reason: Dear designers, Thank you for submitting your work over the last few days. Unfortunately we haven't been able to get back to you regarding the final selection of design as the Author of the book has been away on leave with his family without reliable internet access. He is now back and will be giving feedback as we go. We apologise for the time extension. Unfortunately the site didn’t allow me to limit the extension for less than 5 days but we may not require that long. Thanks again. Lulu

Reason: We apologies we hadn't finalized a decision on this project due to the person from our end being away. We would like to finalise this design as soon as possible.

Target Market(s)

22 - 45 age group. Most fall between 30-40. Both male and female. couples , individuals etc ...

Industry/Entity Type

Finance

Font styles to use
Other font styles liked:
• sabon/Aeriel. Let me know if any other suggestions.

Requirements
Nice to have
• use green colour if possible but not essential.

```html
<!DOCTYPE html>
<html lang="en">
<head>
<meta charset="utf-8">
<title>The Pocket Handbook of Home Lending — Cover</title>
<link rel="stylesheet" href="https://fonts.googleapis.com/css2?family=Open+Sans:wght@400;700;800&family=Source+Sans+3:wght@400;600&family=Cinzel:wght@500&display=swap">
<style>
  :root {
    --teal: #0a5f6c;
    --gold: #f7c600;
    --gold-shade: #c79b00;
    --ink-blue: #2d3d9a;
    --bullet-green: #5fb334;
    --paper: #ffffff;
    --logo-ink: #1f2b36;
  }
  * { margin: 0; padding: 0; box-sizing: border-box; }
  html, body { width: 1200px; height: 850px; overflow: hidden; background: var(--paper); }
  .cover {
    position: relative; width: 1200px; height: 850px; overflow: hidden;
    background: var(--paper);
    font-family: "Source Sans 3", "Helvetica Neue", Arial, sans-serif;
  }
  .band { position: absolute; left: 0; width: 100%; background: var(--teal); }
  .band--top { top: 0; height: 109px; }
  .band--bottom { top: 759px; height: 91px; }

  /* Back cover */
  .back { position: absolute; left: 55px; top: 142px; width: 500px; color: var(--ink-blue); }
  .back__title {
    font-family: "Open Sans", Arial, sans-serif; font-weight: 700;
    font-size: 17px; color: var(--gold); text-align: center; letter-spacing: 0.1px;
    text-transform: uppercase;
  }
  .back__subtitle {
    font-family: "Open Sans", Arial, sans-serif; font-weight: 700;
    font-size: 18.5px; color: var(--teal); text-align: center; margin-top: 11px;
  }
  .back__body { font-size: 13.2px; line-height: 17.5px; margin-top: 15px; }
  .back__body p + p { margin-top: 17.5px; }
  .lessons { list-style: none; }
  .lessons li { position: relative; padding-left: 12px; text-indent: -12px; padding-left: 0; }
  .lessons li::before { content: "•"; color: var(--bullet-green); font-weight: 700; margin-right: 6px; }
  .lessons li.gap { margin-top: 17.5px; }

  .publisher { position: absolute; left: 193px; top: 640px; display: flex; align-items: center; gap: 8px; }
  .publisher__mark { width: 14px; height: 14px; background: var(--teal); }
  .publisher__name {
    font-family: "Source Sans 3", Arial, sans-serif; font-weight: 600;
    font-size: 18px; color: var(--logo-ink);
  }

  /* Front cover */
  .front__title {
    position: absolute; left: 640px; top: 22px; width: 520px;
    font-family: "Open Sans", Arial, sans-serif; font-weight: 800;
    text-transform: uppercase; line-height: 1; text-align: center;
  }
  .front__title span { display: block; }
  .title-gold { color: var(--gold); text-shadow: 2px 2px 0 var(--gold-shade), 3px 4px 4px rgba(0,0,0,.25); }
  .title-line--lead { font-size: 64px; letter-spacing: 1px; }
  .title-line--handbook { font-size: 70px; color: var(--teal); margin-top: 26px; text-shadow: 2px 3px 3px rgba(0,0,0,.2); }
  .title-line--handbook small { font-size: 36px; color: var(--gold); text-transform: none; }
  .title-line--home { font-size: 100px; margin-top: 10px; }
  .title-line--lending { font-size: 98px; margin-top: 2px; }

  .front__art {
    position: absolute; left: 770px; top: 390px; width: 220px; height: 310px;
    border-radius: 6px;
    background: linear-gradient(160deg, #e6e9ec 0%, #b8bfc6 55%, #6f8a5c 100%);
  }
  .front__subtitle {
    position: absolute; left: 640px; top: 708px; width: 520px; text-align: center;
    font-family: "Open Sans", Arial, sans-serif; font-weight: 700;
    font-size: 27px; color: var(--teal); text-transform: uppercase; letter-spacing: 0.8px;
  }
  .front__author {
    position: absolute; left: 640px; top: 780px; width: 520px; text-align: center;
    font-family: "Cinzel", Georgia, serif; font-weight: 500;
    font-size: 36px; color: var(--paper); letter-spacing: 2px;
  }
</style>
</head>
<body>
<main class="cover">
  <div class="band band--top"></div>
  <div class="band band--bottom"></div>

  <section class="back">
    <h2 class="back__title">The pocket handbook of home lending.</h2>
    <p class="back__subtitle">The quiet road to plenty.</p>
    <div class="back__body">
      <p>The number-one reason most investors never own more than one property is finance.<br>
      For them, getting and managing money is the scariest part of investing.<br>
      You must be 100% informed when structuring your loans. Before you even think about finding a property, you must understand the valuation process.</p>
      <p>In simple, jargon-free language, this mini guide arms you with a wealth of knowledge to reduce risk and keep control of your investment goals.<br>
      Its many vital lessons include:</p>
      <ul class="lessons">
        <li>How to keep your own home safe and out of the bank’s hands.</li>
        <li>The first step to successful investing is knowing where you want to finish. Learn how different exit strategies affect your investment plan.</li>
        <li class="gap">The main reason most Australians aren’t wealthy is that they don’t know the difference between appreciating and depreciating assets and beneficial and non-beneficial liabilities. Learn to view everything as one or the other.</li>
        <li class="gap">Grasping the concept of leverage and other people’s money will dramatically increase your return on equity.</li>
        <li class="gap">Banking and finance. By knowing what lenders need to asses a loan, you can apply with confidence and put yourself ahead of the pack.</li>
      </ul>
    </div>
  </section>

  <div class="publisher">
    <span class="publisher__mark"></span>
    <span class="publisher__name">Harbourline Property Education</span>
  </div>

  <h1 class="front__title">
    <span class="title-line--lead title-gold">The Pocket</span>
    <span class="title-line--handbook">Handbook <small>of</small></span>
    <span class="title-line--home title-gold">Home</span>
    <span class="title-line--lending title-gold">Lending</span>
  </h1>

  <div class="front__art" role="img" aria-label="Illustration of a house whose front opens as a steel safe door, with stacks of banknotes inside and spilling out"></div>

  <p class="front__subtitle">The quiet road to plenty</p>
  <p class="front__author">Ned Pargiter</p>
</main>
</body>
</html>
```